Coffee Promotion for Specialty Coffees

I need to have a poster designed to promote our coffee sales. We offer cappuccino for $3.75, Latte for $3.75, Americano for $2.00, Espresso $2.00 and Fair Trade Organic Colombian Coffee for $1.75 Med, $2.00L Large. I would like sometihng very visual that shows the coffees and also has the pricing, and includes the wording" Try our Amazing Specialty Coffees!" Our logo is attached as well

Poster size is 24" wide x 36" high

Target Market(s)

Seniors and Students in a Mall Setting

Colors

Designer to choose colors to be used in the design.

Requirements
Must have
• Graphic artwork of coffees (cappuccinos, lattes, etc). Logo included in artwork. Must be for 24"wide x 36" high poster
Nice to have
• Would like something that shows closeups of the coffees and visually sells the coffee being premium and delicious.

```html
<!DOCTYPE html>
<html lang="en">
<head>
<meta charset="utf-8">
<title>Swirlwell – Specialty Coffees</title>
<link rel="stylesheet" href="https://fonts.googleapis.com/css2?family=Cabin+Sketch:wght@700&family=Archivo+Black&family=Montserrat:wght@800&display=swap">
<style>
  :root {
    --wood-dark: #3a2c25;
    --wood-mid: #6b5a4e;
    --wood-light: #8c7a6b;
    --wood-red: #7a4a40;
    --cream: #fbf6e6;
    --glow: #f4efb8;
    --band-brown: #5a3a1e;
    --label-yellow: #f6ee2a;
    --price-green: #4fb536;
    --price-green-light: #9be07a;
    --price-ink: #e9f2d6;
    --price-outline: #1f3d14;
    --bow-red: #d3201a;
    --logo-dark: #2b2626;
  }
  html, body {
    margin: 0;
    padding: 0;
    width: 800px;
    height: 1200px;
    overflow: hidden;
    background: var(--wood-dark);
  }
  .poster {
    position: relative;
    width: 800px;
    height: 1200px;
    overflow: hidden;
  }
  .poster svg { display: block; }
  .headline {
    font-family: "Cabin Sketch", "Comic Sans MS", cursive;
    font-weight: 700;
    font-size: 56px;
    fill: var(--cream);
    letter-spacing: 1px;
  }
  .brand-name {
    font-family: "Cabin Sketch", "Comic Sans MS", cursive;
    font-weight: 700;
    font-size: 30px;
    fill: var(--cream);
  }
  .item-label {
    font-family: "Montserrat", Arial, sans-serif;
    font-weight: 800;
    font-size: 16px;
    letter-spacing: 3px;
    fill: var(--label-yellow);
  }
  .item-label--small { font-size: 13px; letter-spacing: 2px; }
  .label-band {
    fill: none;
    stroke: var(--band-brown);
    stroke-width: 30;
    stroke-linecap: round;
  }
  .photo-ring {
    fill: none;
    stroke: var(--glow);
    stroke-width: 8;
    opacity: 0.75;
  }
  .price-tag { fill: url(#priceGradient); stroke: var(--glow); stroke-width: 3; }
  .price-text {
    font-family: "Archivo Black", "Arial Black", sans-serif;
    font-size: 50px;
    fill: var(--price-ink);
    stroke: var(--price-outline);
    stroke-width: 2.5px;
    paint-order: stroke;
  }
  .size-note {
    font-family: "Montserrat", Arial, sans-serif;
    font-weight: 800;
    font-size: 10px;
    fill: #111;
  }
  .bow { fill: var(--bow-red); }
</style>
</head>
<body>
<main class="poster">
<svg width="800" height="1200" viewBox="0 0 800 1200" xmlns="http://www.w3.org/2000/svg">
  <defs>
    <linearGradient id="woodGradient" x1="0" y1="0" x2="1" y2="0">
      <stop offset="0" stop-color="#4a3a32"/>
      <stop offset="0.3" stop-color="#6b5a4e"/>
      <stop offset="0.6" stop-color="#5d4c42"/>
      <stop offset="1" stop-color="#7a4a40"/>
    </linearGradient>
    <radialGradient id="priceGradient" cx="0.45" cy="0.35" r="0.7">
      <stop offset="0" stop-color="var(--price-green-light)"/>
      <stop offset="1" stop-color="var(--price-green)"/>
    </radialGradient>
    <radialGradient id="cappuccinoPhoto" cx="0.5" cy="0.4" r="0.6">
      <stop offset="0" stop-color="#e8c08a"/>
      <stop offset="0.45" stop-color="#8a4a26"/>
      <stop offset="1" stop-color="#4a2a18"/>
    </radialGradient>
    <radialGradient id="lattePhoto" cx="0.5" cy="0.45" r="0.6">
      <stop offset="0" stop-color="#e4a05a"/>
      <stop offset="0.5" stop-color="#f3eee8"/>
      <stop offset="1" stop-color="#7a4a2a"/>
    </radialGradient>
    <radialGradient id="americanoPhoto" cx="0.5" cy="0.45" r="0.6">
      <stop offset="0" stop-color="#2a1a12"/>
      <stop offset="0.45" stop-color="#eeeae4"/>
      <stop offset="1" stop-color="#6a4a34"/>
    </radialGradient>
    <radialGradient id="espressoPhoto" cx="0.5" cy="0.55" r="0.6">
      <stop offset="0" stop-color="#a8733e"/>
      <stop offset="0.45" stop-color="#3a2a20"/>
      <stop offset="1" stop-color="#141414"/>
    </radialGradient>
    <radialGradient id="colombianPhoto" cx="0.5" cy="0.5" r="0.6">
      <stop offset="0" stop-color="#f4f0ea"/>
      <stop offset="0.45" stop-color="#8a5a34"/>
      <stop offset="1" stop-color="#3a2216"/>
    </radialGradient>
    <radialGradient id="logoGlow" cx="0.5" cy="0.5" r="0.5">
      <stop offset="0.7" stop-color="#c05aa0" stop-opacity="0.6"/>
      <stop offset="1" stop-color="#c05aa0" stop-opacity="0"/>
    </radialGradient>
    <path id="labelArc" d="M 33 -124 A 128 128 0 0 1 124 33"/>
    <path id="labelArcLong" d="M 11 -132 A 132 132 0 0 1 101 85"/>
  </defs>

  <rect class="backdrop" width="800" height="1200" fill="url(#woodGradient)" role="img" aria-label="Weathered wooden plank background"/>

  <!-- Brand mark -->
  <g class="brand">
    <circle cx="116" cy="100" r="96" fill="url(#logoGlow)"/>
    <circle cx="116" cy="100" r="80" fill="var(--logo-dark)"/>
    <text class="brand-name" x="116" y="110" text-anchor="middle">Swirlwell</text>
  </g>

  <!-- Headline -->
  <text class="headline" x="500" y="98" text-anchor="middle">TRY OUR AMAZING</text>
  <text class="headline" x="492" y="166" text-anchor="middle">SPECIALTY COFFEES!</text>

  <!-- Cappuccino -->
  <g class="menu-item" transform="translate(172 344)">
    <path class="label-band" d="M 33 -124 A 128 128 0 0 1 124 33"/>
    <text class="item-label"><textPath href="#labelArc" startOffset="50%" text-anchor="middle" dominant-baseline="middle">CAPPUCCINO</textPath></text>
    <circle r="112" fill="url(#cappuccinoPhoto)" role="img" aria-label="Cappuccino with leaf latte art in a brown cup"/>
    <circle class="photo-ring" r="114"/>
    <circle class="bow" cx="-78" cy="-84" r="30" role="img" aria-label="Red gift bow"/>
    <ellipse class="price-tag" cx="116" cy="120" rx="96" ry="44"/>
    <text class="price-text" x="116" y="138" text-anchor="middle">$3.75</text>
  </g>

  <!-- Latte -->
  <g class="menu-item" transform="translate(564 344)">
    <path class="label-band" d="M 33 -124 A 128 128 0 0 1 124 33"/>
    <text class="item-label"><textPath href="#labelArc" startOffset="50%" text-anchor="middle" dominant-baseline="middle">LATTE</textPath></text>
    <circle r="112" fill="url(#lattePhoto)" role="img" aria-label="Latte with heart latte art in a white cup"/>
    <circle class="photo-ring" r="114"/>
    <circle class="bow" cx="-68" cy="-84" r="30" role="img" aria-label="Red gift bow"/>
    <ellipse class="price-tag" cx="96" cy="120" rx="96" ry="44"/>
    <text class="price-text" x="96" y="138" text-anchor="middle">$3.75</text>
  </g>

  <!-- Americano -->
  <g class="menu-item" transform="translate(164 684)">
    <path class="label-band" d="M 33 -124 A 128 128 0 0 1 124 33"/>
    <text class="item-label"><textPath href="#labelArc" startOffset="50%" text-anchor="middle" dominant-baseline="middle">AMERICANO</textPath></text>
    <circle r="112" fill="url(#americanoPhoto)" role="img" aria-label="Black americano in a white cup with saucer and spoon"/>
    <circle class="photo-ring" r="114"/>
    <circle class="bow" cx="-80" cy="-84" r="30" role="img" aria-label="Red gift bow"/>
    <ellipse class="price-tag" cx="124" cy="116" rx="96" ry="44"/>
    <text class="price-text" x="124" y="134" text-anchor="middle">$2.00</text>
  </g>

  <!-- Espresso -->
  <g class="menu-item" transform="translate(564 696)">
    <path class="label-band" d="M 33 -124 A 128 128 0 0 1 124 33"/>
    <text class="item-label"><textPath href="#labelArc" startOffset="50%" text-anchor="middle" dominant-baseline="middle">ESPRESSO</textPath></text>
    <circle r="112" fill="url(#espressoPhoto)" role="img" aria-label="Espresso in a clear glass cup on a steel saucer"/>
    <circle class="photo-ring" r="114"/>
    <circle class="bow" cx="-72" cy="-84" r="30" role="img" aria-label="Red gift bow"/>
    <ellipse class="price-tag" cx="100" cy="112" rx="96" ry="44"/>
    <text class="price-text" x="100" y="130" text-anchor="middle">$2.00</text>
  </g>

  <!-- Colombian Coffee -->
  <g class="menu-item" transform="translate(404 996)">
    <path class="label-band" d="M 11 -132 A 132 132 0 0 1 101 85"/>
    <text class="item-label item-label--small"><textPath href="#labelArcLong" startOffset="50%" text-anchor="middle" dominant-baseline="middle">COLOMBIAN COFFEE</textPath></text>
    <circle r="116" fill="url(#colombianPhoto)" role="img" aria-label="Colombian coffee in a white cup with beans, cinnamon sticks and star anise"/>
    <circle class="photo-ring" r="118"/>
    <circle class="bow" cx="-68" cy="-100" r="30" role="img" aria-label="Red gift bow"/>
    <ellipse class="price-tag" cx="-128" cy="120" rx="102" ry="46"/>
    <text class="price-text" x="-128" y="138" text-anchor="middle">$2.00</text>
    <text class="size-note" x="-128" y="158" text-anchor="middle">(LARGE)</text>
    <ellipse class="price-tag" cx="148" cy="120" rx="102" ry="46"/>
    <text class="price-text" x="148" y="138" text-anchor="middle">$1.75</text>
    <text class="size-note" x="148" y="158" text-anchor="middle">(MEDIUM)</text>
  </g>
</svg>
</main>
</body>
</html>
```